Kelvo Cube needs a packaging design

Hello!

I need an eye-catching package design for Kelvo Cube mobile accessories. The products inside the box package include a bluetooth speaker and a power bank.

This is under our brandname called Kelvo Cube. The text should be in the picture, no matter how the design looks.

I have attached pictures of the products. If you think that there will not be well with the images it is ok. Then these texts be included:
Bluetooth Speaker
Power Bank

This is our slogan:
Music + Power. It's your imagination that sets the limits!

The image will be printed on a carton pack containing with four color printing. Customising the picture for the type of print.

Should be in 300 DPI High resolution.

Please check the attached pictures where your design will be printed.
Also, I attached design inspiration images for reference. Feel free to do something similar like that.

For the size and dimensions please refer to this attachment:

So remember, the important thing is the design. Do your absolute best!

Reason: Hello everyone! I would like to see a design without the images of the accessories. Only text. I also dont want the text "Its you imagination that sets...". Thank you!

Target Market(s)

Mobile accessories

Industry/Entity Type

Electronics

Requirements
Must have
• This text:
• Kelvo Cube
Nice to have
• Music + Power.

```html
<!DOCTYPE html>
<html lang="en">
<head>
<meta charset="utf-8">
<title>Kelvo Cube – Packaging Dieline</title>
<link rel="stylesheet" href="https://fonts.googleapis.com/css2?family=Exo+2:ital,wght@1,700;1,800&display=swap">
<style>
  :root {
    --ink: #03040a;
    --navy: #0a0f2e;
    --cut: #ffffff;
    --type: #f4f7ff;
    --glow: #2f8cff;
    --glow-soft: rgba(60, 140, 255, 0.75);
  }
  html, body {
    margin: 0;
    padding: 0;
    width: 1200px;
    height: 1200px;
    overflow: hidden;
    background: var(--cut);
  }
  .dieline {
    position: relative;
    width: 1200px;
    height: 1200px;
    background: var(--ink);
    overflow: hidden;
  }
  .artwork {
    position: absolute;
    inset: 0;
  }
  .corner-cut {
    position: absolute;
    width: 180px;
    height: 180px;
    background: var(--cut);
  }
  .corner-cut.tl { left: 0; top: 0; }
  .corner-cut.tr { right: 0; top: 0; }
  .corner-cut.bl { left: 0; bottom: 0; }
  .corner-cut.br { right: 0; bottom: 0; }

  .glow-type {
    color: var(--type);
    text-shadow: 0 0 6px var(--glow), 0 0 14px var(--glow-soft), 0 0 26px var(--glow-soft);
    white-space: nowrap;
    margin: 0;
  }

  .brand-title {
    font-family: "Exo 2", sans-serif;
    font-style: italic;
    font-weight: 800;
    text-transform: uppercase;
  }
  .product-line {
    font-family: "Exo 2", sans-serif;
    font-style: italic;
    font-weight: 800;
  }

  .front-lockup {
    position: absolute;
    left: 214px;
    top: 636px;
    transform: rotate(-10deg);
    transform-origin: left top;
  }
  .front-lockup .brand-title {
    font-size: 54px;
    letter-spacing: 50px;
    line-height: 1;
  }
  .front-lockup .product-line {
    font-size: 32px;
    letter-spacing: 8px;
    margin: 2px 0 0 52px;
    line-height: 1;
  }

  .range-note {
    position: absolute;
    left: 630px;
    width: 360px;
    top: 894px;
    font-family: "Exo 2", sans-serif;
    font-style: italic;
    font-weight: 800;
    font-size: 20px;
    letter-spacing: 17px;
    line-height: 46px;
    text-align: center;
  }

  .flap-lockup {
    position: absolute;
    left: 180px;
    width: 840px;
    top: 1074px;
    text-align: center;
  }
  .flap-lockup .brand-title {
    font-size: 48px;
    letter-spacing: 36px;
    line-height: 1;
  }
  .flap-lockup .product-line {
    font-size: 26px;
    letter-spacing: 6px;
    line-height: 1;
    margin-top: 4px;
  }

  .slogan {
    position: absolute;
    font-family: "Exo 2", sans-serif;
    font-style: italic;
    font-weight: 800;
    font-size: 28px;
    line-height: 28px;
  }
  .side-left { left: 128px; top: 224px; transform: rotate(90deg); transform-origin: left top; }
  .side-right { left: 1066px; top: 968px; transform: rotate(-90deg); transform-origin: left top; }
</style>
</head>
<body>
  <main class="dieline">
    <svg class="artwork" width="1200" height="1200" viewBox="0 0 1200 1200" role="img" aria-label="Dark background with a photograph of swirling blue and white light trails and a faint speaker grille">
      <defs>
        <radialGradient id="lightTrails" cx="330" cy="270" r="420" gradientUnits="userSpaceOnUse">
          <stop offset="0" stop-color="#6a8fd0" stop-opacity="0.75"/>
          <stop offset="0.35" stop-color="#1d4fc4" stop-opacity="0.45"/>
          <stop offset="1" stop-color="#03040a" stop-opacity="0"/>
        </radialGradient>
        <radialGradient id="speakerHaze" cx="760" cy="680" r="480" gradientUnits="userSpaceOnUse">
          <stop offset="0" stop-color="#101638" stop-opacity="0.9"/>
          <stop offset="1" stop-color="#03040a" stop-opacity="0"/>
        </radialGradient>
      </defs>
      <rect width="1200" height="1200" fill="#03040a"/>
      <rect width="1200" height="1200" fill="url(#speakerHaze)"/>
      <rect width="1200" height="1200" fill="url(#lightTrails)"/>
    </svg>

    <div class="corner-cut tl"></div>
    <div class="corner-cut tr"></div>
    <div class="corner-cut bl"></div>
    <div class="corner-cut br"></div>

    <p class="slogan side-left glow-type">Music + Power</p>

    <section class="front-lockup">
      <h1 class="brand-title glow-type">Kelvo Cube</h1>
      <p class="product-line glow-type">bluetooth speaker+power bank</p>
    </section>

    <p class="range-note glow-type">All mobile<br>accessories</p>

    <p class="slogan side-right glow-type">Music + Power</p>

    <section class="flap-lockup">
      <h2 class="brand-title glow-type">Kelvo Cube</h2>
      <p class="product-line glow-type">bluetooth speaker+power bank</p>
    </section>
  </main>
</body>
</html>
```